Personal Trainer website design

We are working with a personal trainer to design a website. They offer their primary services: Diet Coaching, In-Person Coaching (workouts), and Remote Coaching.
Some sites we like: https://www.mirabelfenn.com, https://kitarowe.com/en-us, https://bendwellstudio.co.uk
Thank you for taking the time to consider designing a website for us. We are web developers based in Stockton, CA USA. Most of our projects go through the same process. Understanding this process may help you win a project with us. We custom-code all of our websites in-house. We don’t have any requirements as to what tools you use for your design, but ask that you follow these guidelines.
IMAGES:
We ask that if you use any images, or icons in the design, have a link to the asset, so we can purchase the image/icon. Most of the designs we submit do not have the customer’s images on them unless they have some great images. Be creative; show us the feeling that you are trying to portray with your image choices. Use any royalty-free site you choose. We subscribe to Quillon and mostly use their images, but are ok to purchase images outside of Quillon.
FONTS:
We ask that you identify the fonts you’re using in the design. This can be done in a message if you want. We typically use Tembrik Fonts and Quillon Fonts.
CONTENT:
We're always open to different content and ideas. Often, we submit designs with stock images so that the client can see our vision. We typically go back and take pictures after the website launch to use their images with our vision. Lorem Ipsum is fine for paragraphs, but we ask that you make the Headers with correct English. We want to be able to show the vision and identify the sections of the website.
INSPIRATION:
We try and add a couple of links in the brief of some websites that we like to help you get started in your design.
REVISIONS:
We do not often ask for revisions of the designs unless we see something in the design that may not appeal to the client. If there are slight changes that we want to make, we simply do that in the development process.
FEEDBACK:
We rarely give feedback on designs during the design process. We are working on many website projects and do not have the time to give feedback. We usually respond if your request is well thought out and asks specific questions, but a note asking “feedback, please” usually goes unanswered.

```html
<!DOCTYPE html>
<html lang="en">
<head>
<meta charset="utf-8">
<title>Orbitfit — Personal Training</title>
<link href="https://fonts.googleapis.com/css2?family=Bebas+Neue&family=Poppins:wght@400;500&display=swap" rel="stylesheet">
<style>
:root{
  --green:#8b9a1c;
  --green-dark:#6f7c12;
  --black:#0d0d0d;
  --panel:#2a2a28;
  --white:#ffffff;
  --text:#1a1a1a;
  --offer:#f2d21c;
}
*{box-sizing:border-box;margin:0;padding:0}
html,body{width:1200px;height:3250px;overflow:hidden;background:var(--white)}
body{position:relative;font-family:"Poppins",sans-serif;color:var(--text)}
.abs{position:absolute}
.photo{position:absolute;overflow:hidden}
.disc{position:absolute;border-radius:50%}

/* header */
.site-header{position:absolute;left:0;top:0;width:1200px;height:152px;background:var(--white)}
.brand{position:absolute;left:30px;top:52px;display:flex;align-items:center;gap:10px;font-family:"Bebas Neue",sans-serif;font-size:72px;color:var(--text);line-height:1}
.brand-dot{width:18px;height:18px;border-radius:50%;background:var(--green)}
.speak{position:absolute;left:628px;top:46px;font-family:"Bebas Neue",sans-serif;font-size:25px}
.phone-pill{position:absolute;left:933px;top:36px;width:207px;height:42px;border-radius:21px;background:var(--green);color:var(--white);font-family:"Bebas Neue",sans-serif;font-size:25px;text-align:center;line-height:44px}
.nav{position:absolute;left:356px;top:96px;display:flex;gap:21px;font-size:18px}
.nav a{color:var(--text);text-decoration:none}
.nav a.active{color:var(--green)}

/* hero */
.hero{position:absolute;left:0;top:152px;width:1200px;height:660px;background:var(--black);overflow:hidden}
.hero-title{position:absolute;left:737px;top:58px;font-family:"Bebas Neue",sans-serif;font-size:64px;line-height:70px;color:var(--green);font-weight:400}
.hero-title span{color:var(--white)}
.feature-list{position:absolute;left:738px;top:212px;list-style:none}
.feature-list li{display:flex;align-items:center;gap:18px;height:68px;color:var(--white);font-size:19px}
.bullet{width:30px;height:30px;border-radius:50%;background:var(--green);flex:none}
.hero-cta{position:absolute;left:744px;top:510px;font-size:23px;line-height:31px;color:var(--green);font-weight:500;letter-spacing:.5px}
.hero-cta span{color:var(--white)}

/* service tiles */
.tile{position:absolute;top:812px;height:415px;background:var(--panel);overflow:hidden}
.tile-label{position:absolute;left:0;width:100%;height:65px;background:var(--panel);color:var(--green);font-family:"Bebas Neue",sans-serif;font-size:32px;text-align:center;line-height:68px}

/* why choose */
.section-title{font-family:"Bebas Neue",sans-serif;font-size:32px;color:var(--text);font-weight:400}
.section-sub{font-size:24px;color:var(--green);line-height:31px;font-weight:500}
.why-list{position:absolute;left:60px;top:1450px;list-style:none}
.why-list li{display:flex;align-items:center;gap:20px;font-size:19px;line-height:25px}
.btn{position:absolute;background:var(--green);color:var(--white);font-family:"Bebas Neue",sans-serif;text-align:center;border-radius:24px}
.offer{position:absolute;left:800px;top:1378px;width:325px;text-align:center;font-family:"Bebas Neue",sans-serif;font-size:50px;line-height:52px;color:var(--offer)}

/* steps */
.step-num{position:absolute;top:1945px;font-family:"Bebas Neue",sans-serif;font-size:118px;line-height:1;color:var(--green)}
.step-text{position:absolute;top:1952px;font-size:19px;line-height:24.5px}

/* testimonial */
.quote{position:absolute;left:552px;top:2322px;width:610px;font-size:19px;line-height:24.5px}

/* footer */
.site-footer{position:absolute;left:0;top:2670px;width:1200px;height:580px;background:var(--black);color:var(--white);overflow:hidden}
.footer-brand{position:absolute;left:62px;top:60px;display:flex;align-items:center;gap:10px;font-family:"Bebas Neue",sans-serif;font-size:66px;color:var(--white);line-height:1}
.footer-heading{position:absolute;font-family:"Bebas Neue",sans-serif;font-size:32px;color:var(--green)}
.footer-text{position:absolute;font-size:15px;line-height:26px}
.footer-text b{color:var(--green);font-weight:400}
.mid-panel{position:absolute;left:500px;top:0;width:265px;height:372px;background:#161616}
.socials{position:absolute;left:520px;top:323px;display:flex;gap:18px}
.socials span{width:40px;height:40px;border-radius:50%;border:2px solid var(--white)}
.form-label{position:absolute;left:910px;font-size:15px}
.form-input{position:absolute;left:911px;width:215px;border:1px solid var(--white)}
</style>
</head>
<body>

<header class="site-header">
  <div class="brand"><span>Orbitfit</span><span class="brand-dot"></span></div>
  <div class="speak">Speak to our friendly experts:</div>
  <div class="phone-pill">1.555.010.2468</div>
  <nav class="nav">
    <a class="active">HOME</a><a>ABOUT US</a><a>OUR TRAINERS</a><a>OUR PROGRAMS▾</a><a>TESTIMONIALS</a><a>CONTACT US</a>
  </nav>
</header>

<section class="hero">
  <div class="disc" style="left:-10px;top:6px;width:718px;height:718px;background:var(--green-dark)"></div>
  <div class="disc" style="left:-30px;top:10px;width:710px;height:710px;background:var(--green)"></div>
  <div class="photo" role="img" aria-label="Smiling man and woman in workout clothes flexing their arms" style="left:0;top:80px;width:700px;height:580px;border-radius:48% 48% 0 0;background:radial-gradient(ellipse at 45% 40%,#c08f6c 0%,#8a6048 35%,rgba(40,30,26,.9) 70%,rgba(139,154,28,0) 90%)"></div>
  <h1 class="hero-title">Personal Training<br>That <span>Works for You</span></h1>
  <ul class="feature-list">
    <li><span class="bullet"></span>Customised workouts</li>
    <li><span class="bullet"></span>In-person training sessions</li>
    <li><span class="bullet"></span>Remote training sessions</li>
    <li><span class="bullet"></span>Practical, effective diet plans</li>
  </ul>
  <div class="hero-cta">BOOK YOUR <span>FREE</span><br>CONSULTATION TODAY&gt;&gt;</div>
</section>

<div class="tile" style="left:0;width:398px">
  <div class="tile-label" style="top:0">Face-to-Face Training &gt;</div>
  <div class="photo" role="img" aria-label="Older man lifting a barbell with his trainer in a gym" style="left:0;top:65px;width:398px;height:350px;background:linear-gradient(100deg,#3f6ea8 0%,#9b8578 40%,#c9a489 55%,#2f5fa8 100%)"></div>
</div>
<div class="tile" style="left:401px;width:401px">
  <div class="photo" role="img" aria-label="Woman doing a core exercise on a living room floor" style="left:0;top:0;width:401px;height:350px;background:linear-gradient(180deg,#8c8c8a 0%,#5a5a58 45%,#2e2e2d 70%,#b8b8b6 100%)"></div>
  <div class="tile-label" style="top:350px">Remote Training &gt;</div>
</div>
<div class="tile" style="left:805px;width:395px">
  <div class="tile-label" style="top:0">Customised Diet Plans &gt;</div>
  <div class="photo" role="img" aria-label="Hands holding a bowl of salad with avocado" style="left:0;top:65px;width:395px;height:350px;background:radial-gradient(circle at 55% 50%,#7a9a3a 0%,#5d7530 30%,#4a4a46 55%,#5c5c58 100%)"></div>
</div>

<h2 class="section-title abs" style="left:60px;top:1310px">Why Choose Us</h2>
<p class="section-sub abs" style="left:60px;top:1354px">Orbitfit Recognises that Everyone is Different,<br>so One Solution Does not Fit All</p>
<ul class="why-list">
  <li style="height:50px"><span class="bullet"></span>We work with you one-on-one</li>
  <li style="height:68px"><span class="bullet"></span>Your goals become ours</li>
  <li style="height:82px"><span class="bullet"></span>We offer a wholesome plan including<br>diet plans &amp; workouts</li>
  <li style="height:82px"><span class="bullet"></span>Your trainer will work around<br>your availability</li>
</ul>
<div class="btn" style="left:63px;top:1752px;width:208px;height:41px;font-size:24px;line-height:44px">Get Started Today!</div>

<div class="disc" style="left:725px;top:1315px;width:560px;height:560px;background:var(--green-dark)"></div>
<div class="disc" style="left:735px;top:1325px;width:550px;height:550px;background:var(--green)"></div>
<div class="photo" role="img" aria-label="Black dumbbell with stacked weight plates" style="left:690px;top:1520px;width:480px;height:330px;background:radial-gradient(ellipse 50% 46% at 50% 52%,#6e6e6e 0%,#333 55%,#222 80%,rgba(34,34,34,0) 100%)"></div>
<div class="offer">Get 10% Off<br>Your First<br>Session!</div>

<h2 class="section-title abs" style="left:70px;top:1890px">How It Works</h2>
<div class="step-num" style="left:66px">1</div>
<div class="step-text" style="left:116px">Initial consultation<br>to assess your<br>fitness, goals, &amp;<br>lifestyle</div>
<div class="step-num" style="left:318px">2</div>
<div class="step-text" style="left:381px">Tailor a program<br>to include a diet<br>plan &amp; workout<br>schedule</div>
<div class="step-num" style="left:558px">3</div>
<div class="step-text" style="left:627px">Get you started on<br>your workouts &amp;<br>diet with atleast 3<br>sessions a week</div>
<div class="step-num" style="left:830px">4</div>
<div class="step-text" style="left:901px">Fortnightly assessments<br>to ensure you are on<br>track to meet your goals<br>successfully</div>

<div class="abs" style="left:0;top:2160px;width:520px;height:510px;overflow:hidden">
  <div class="disc" style="left:-22px;top:6px;width:534px;height:534px;background:var(--green-dark)"></div>
  <div class="disc" style="left:-30px;top:12px;width:524px;height:524px;background:var(--green)"></div>
</div>
<div class="photo" role="img" aria-label="Trainer guiding a woman through a forward stretch" style="left:60px;top:2120px;width:430px;height:550px;border-radius:45% 45% 10% 10%;background:radial-gradient(ellipse 50% 50% at 50% 45%,#2b55b8 0%,#6aa8c0 30%,#2a2a2a 60%,rgba(42,42,42,0) 100%)"></div>
<h2 class="section-title abs" style="left:551px;top:2180px">What Our Clients Have to Say</h2>
<p class="section-sub abs" style="left:551px;top:2225px">We Know We have a Great Team, but Don’t<br>Take Our Word for it</p>
<p class="quote">“ I have been struggling with my weight for years,<br>and had given up hope of ever becoming fit. It just seemed<br>so difficult. Then I learnt about Orbitfit - I have been working<br>with Marcus for 6 months now, and have already lost 10 kgs,<br>feel great, and have more energy.<br>Can’t thank Orbitfit enough, they know what they are doing.”<br>- Della Marsh</p>
<div class="btn" style="left:551px;top:2522px;width:412px;height:48px;font-size:26px;line-height:52px">Sign Up for the Orbitfit Advantage</div>

<footer class="site-footer">
  <div class="photo" role="img" aria-label="Yellow measuring tape curling around a green apple" style="left:0;top:320px;width:480px;height:260px;background:radial-gradient(ellipse 60% 40% at 40% 55%,rgba(200,170,20,.8) 0%,rgba(120,100,10,.4) 50%,rgba(13,13,13,0) 100%)"></div>
  <div class="mid-panel"></div>
  <div class="footer-brand"><span>Orbitfit</span><span class="brand-dot"></span></div>
  <div class="footer-heading" style="left:62px;top:178px">Get in Touch</div>
  <div class="footer-text" style="left:62px;top:236px"><b>P:</b> 1.555.010.2469<br><b>E:</b> contact@orbitfit.com</div>

  <div class="footer-heading" style="left:520px;top:82px">What We Do</div>
  <div class="footer-text" style="left:520px;top:143px">Face-to-face Training<br>Remote Training<br>Diet Plans</div>
  <div class="footer-heading" style="left:520px;top:245px">Connect With Us</div>
  <div class="socials"><span></span><span></span><span></span><span></span></div>

  <div class="footer-heading" style="left:910px;top:82px">Reach Out</div>
  <div class="form-label" style="top:148px">Full Name:</div>
  <div class="form-input" style="top:170px;height:38px"></div>
  <div class="form-label" style="top:226px">Phone:</div>
  <div class="form-input" style="top:248px;height:38px"></div>
  <div class="form-label" style="top:305px">Query Details:</div>
  <div class="form-input" style="top:328px;height:56px"></div>
  <div class="btn" style="left:910px;top:404px;width:127px;height:42px;font-family:'Poppins',sans-serif;font-size:14px;line-height:42px">SUBMIT</div>
</footer>

</body>
</html>
```